Logo for Law Office
K. Morland Law
Creative Brief
Professional
Luis T. Fenwick
Attorney at Law
4870 Dunmore St. Suite C-07 Corpus Christi, TX 78401
luisfenwick7@mailvista.com

```html
<!DOCTYPE html>
<html lang="en">
<head>
<meta charset="utf-8">
<title>K. Morland Law – Business Card</title>
<link href="https://fonts.googleapis.com/css2?family=Source+Sans+3:wght@400;600;700&display=swap" rel="stylesheet">
<style>
  :root {
    --page-bg: #d9d9d9;
    --card-black: #0b0b0b;
    --card-black-soft: #1c1c1c;
    --gold-light: #f4cf55;
    --gold: #e2ac2a;
    --gold-deep: #b97f12;
    --silver: #f2f2f2;
    --silver-shade: #9a9a9a;
    --ink: #141414;
    --muted: #b7b7b7;
  }
  * { margin: 0; padding: 0; box-sizing: border-box; }
  html, body {
    width: 1200px; height: 780px; overflow: hidden;
    background: var(--page-bg);
    font-family: "Source Sans 3", "Helvetica Neue", Arial, sans-serif;
  }
  .card {
    position: relative;
    width: 1200px; height: 780px;
    border-radius: 36px;
    overflow: hidden;
  }
  .card-art { position: absolute; inset: 0; }
  .holder {
    position: absolute; left: 96px; top: 120px;
  }
  .holder-name {
    color: var(--gold-light);
    font-weight: 700; font-size: 44px; line-height: 1.1;
  }
  .holder-title {
    color: var(--muted);
    font-size: 27px; margin-top: 8px;
  }
  .brand {
    position: absolute; left: 150px; top: 420px;
    width: 420px; text-align: center;
  }
  .brand-name {
    color: var(--gold);
    font-weight: 600; font-size: 50px;
    letter-spacing: 2px; text-transform: uppercase;
    white-space: nowrap;
  }
  .brand-rule {
    height: 2px; width: 300px; margin: 10px auto 0;
    background: linear-gradient(90deg, transparent, var(--gold), transparent);
  }
  .contacts {
    position: absolute; right: 62px; top: 520px;
    list-style: none; text-align: right;
    color: var(--ink); font-size: 25px;
  }
  .contacts li {
    display: flex; justify-content: flex-end; align-items: center;
    gap: 12px; height: 38px;
  }
  .contacts svg { width: 22px; height: 22px; fill: var(--ink); }
  .address {
    position: absolute; right: 62px; top: 680px;
    color: var(--ink); font-size: 27px;
  }
</style>
</head>
<body>
<div class="card">
  <svg class="card-art" viewBox="0 0 1200 780" width="1200" height="780" aria-hidden="true">
    <defs>
      <linearGradient id="goldFill" x1="0" y1="1" x2="1" y2="0">
        <stop offset="0" stop-color="#c98d16"/>
        <stop offset="0.45" stop-color="#f4cf55"/>
        <stop offset="0.75" stop-color="#e2ac2a"/>
        <stop offset="1" stop-color="#b97f12"/>
      </linearGradient>
      <linearGradient id="blackFill" x1="0" y1="0" x2="1" y2="1">
        <stop offset="0" stop-color="#1c1c1c"/>
        <stop offset="0.6" stop-color="#0b0b0b"/>
        <stop offset="1" stop-color="#000"/>
      </linearGradient>
      <linearGradient id="silverEdge" x1="0" y1="1" x2="1" y2="0">
        <stop offset="0" stop-color="#9a9a9a"/>
        <stop offset="0.5" stop-color="#ffffff"/>
        <stop offset="1" stop-color="#c8c8c8"/>
      </linearGradient>
    </defs>
    <rect class="gold-field" width="1200" height="780" fill="url(#goldFill)"/>
    <path class="silver-sweep" d="M0,0 H1200 V52 C990,62 900,320 740,480 C580,640 390,760 130,780 H0 Z" fill="url(#silverEdge)"/>
    <path class="black-field" d="M0,0 H1200 V30 C980,40 880,300 720,460 C560,620 370,745 100,780 H0 Z" fill="url(#blackFill)"/>
  </svg>

  <div class="holder">
    <h1 class="holder-name">Luis T. Fenwick</h1>
    <p class="holder-title">Attorney at Law</p>
  </div>

  <div class="brand">
    <p class="brand-name">K. Morland Law</p>
    <div class="brand-rule"></div>
  </div>

  <ul class="contacts">
    <li>361-555-0142
      <svg viewBox="0 0 24 24"><path d="M6.6 10.8a15.1 15.1 0 0 0 6.6 6.6l2.2-2.2c.3-.3.7-.4 1-.2 1.1.4 2.3.6 3.6.6.6 0 1 .4 1 1V20c0 .6-.4 1-1 1A17 17 0 0 1 3 4c0-.6.4-1 1-1h3.5c.6 0 1 .4 1 1 0 1.3.2 2.5.6 3.6.1.3 0 .7-.2 1z"/></svg>
    </li>
    <li>361-555-0187
      <svg viewBox="0 0 24 24"><path d="M6 2h10v5H6zM3 8h18v10h-3v4H6v-4H3zm5 7v5h8v-5zm9-5a1 1 0 1 0 0 2 1 1 0 0 0 0-2z"/></svg>
    </li>
    <li>luisfenwick7@mailvista.com
      <svg viewBox="0 0 24 24"><path d="M2 5h20v14H2zm2 2v.5l8 5 8-5V7zm0 2.8V17h16V9.8l-8 5z"/></svg>
    </li>
  </ul>

  <p class="address">4870 Dunmore St. Suite C-07, Corpus Christi, TX 78401</p>
</div>
</body>
</html>
```